Tidewell Works's Facebook Cover Design

I am in need of a social media cover for my company's Facebook account. Please leverage the green logos and color palette attached.

Tidewell Works offers 2 primary services:
1.) Business Automation Services
2.) AI (artificial intelligence integrations)

While a lot of what we do is highly technical, what we deliver is not. In a nutshell, we help our clients to connect their data regardless of what application that data is sitting in. Because we can connect that data, often times we can:

A.) offer more intelligent marketing and help our client increase their revenue.
B.) automate highly repetitive tasks using technology and drive down their costs thus saving them money
C.) help our clients use AI to better serve their customers

You can read a little bit about our company here: https://www.tidewellworks.example

Our tagline is: "Connect data to increase the flow of profitability."

Visually, we'd like your help to illustrate the "connecting" of these applications. Please let me know if you have any questions.

Target Market(s)

Business Owners or Marketing Managers

Industry/Entity Type

Marketing technologies.

Font styles to use
Sans Serif

Requirements
Must have
• Please make every effort to have the cover compatible with the color palette of the attached images.
Should not have
• Please do not use the standard clipart or stock libraries of AI = robot. If you do, please make them small. We help business glue their data from different sources to solve real work problems. Little robots are overused.

```html
<!DOCTYPE html>
<html lang="en">
<head>
<meta charset="utf-8">
<title>Tidewell Works – Facebook Cover</title>
<link href="https://fonts.googleapis.com/css2?family=Red+Hat+Display:wght@400;500;800&display=swap" rel="stylesheet">
<style>
  :root {
    --page-bg: #c2c2c2;
    --green: #84bb58;
    --green-dark: #78b04c;
    --green-light: #9fd074;
    --white: #ffffff;
    --line: rgba(214, 240, 180, 0.75);
    --ink-grey: #55585c;
  }
  * { margin: 0; padding: 0; box-sizing: border-box; }
  html, body {
    width: 1200px;
    height: 1200px;
    overflow: hidden;
    background: var(--page-bg);
    font-family: "Red Hat Display", Arial, sans-serif;
  }
  .cover {
    position: absolute;
    left: 73px;
    top: 372px;
    width: 1052px;
    height: 400px;
    overflow: hidden;
    background:
      radial-gradient(ellipse at 75% 55%, rgba(180, 226, 140, 0.45), transparent 55%),
      linear-gradient(135deg, var(--green-dark), var(--green) 45%, var(--green-dark));
    color: var(--white);
  }
  .cover__lines {
    position: absolute;
    inset: 0;
    width: 100%;
    height: 100%;
  }
  .brand {
    position: absolute;
    left: 85px;
    top: 55px;
    display: flex;
    align-items: center;
    gap: 8px;
    font-size: 28px;
    font-weight: 800;
    letter-spacing: -0.5px;
  }
  .brand__dot {
    width: 12px;
    height: 12px;
    border-radius: 50%;
    background: var(--white);
  }
  .tagline {
    position: absolute;
    left: 85px;
    top: 106px;
    font-size: 46px;
    font-weight: 800;
    line-height: 45px;
    letter-spacing: -0.3px;
    text-transform: uppercase;
  }
  .services {
    position: absolute;
    left: 84px;
    top: 250px;
    font-size: 21px;
    font-weight: 400;
    line-height: 30px;
  }
  .services__list {
    list-style: none;
  }
  .services__item {
    display: flex;
    align-items: center;
    gap: 17px;
  }
  .services__icon {
    width: 22px;
    height: 22px;
    flex: none;
  }
  .illustration {
    position: absolute;
    left: 641px;
    top: 25px;
    width: 332px;
    height: 354px;
    border-radius: 12px;
    background: linear-gradient(160deg, rgba(255,255,255,0.55), rgba(225,225,225,0.35) 55%, rgba(85,88,92,0.35));
  }
</style>
</head>
<body>
  <main class="cover">
    <svg class="cover__lines" viewBox="0 0 1052 400" aria-hidden="true">
      <path d="M667 0 L1000 330" stroke="var(--line)" stroke-width="1" fill="none"/>
      <path d="M825 0 C880 60 940 120 1052 70" stroke="var(--line)" stroke-width="1" fill="none"/>
      <path d="M0 150 C80 140 130 170 180 230" stroke="var(--line)" stroke-width="1" fill="none"/>
      <path d="M0 293 C70 285 110 300 155 400" stroke="var(--line)" stroke-width="1" fill="none"/>
      <path d="M150 280 L310 400" stroke="var(--line)" stroke-width="1" fill="none"/>
      <path d="M960 250 C1000 240 1030 220 1052 195" stroke="var(--line)" stroke-width="1" fill="none"/>
    </svg>

    <div class="brand">
      <span class="brand__dot"></span>
      <span class="brand__name">Tidewell Works</span>
    </div>

    <h1 class="tagline">Connect data to<br>increase the flow<br>of profitability.</h1>

    <section class="services">
      <p class="services__intro">Tidewell Works offers 2 primary services:</p>
      <ul class="services__list">
        <li class="services__item">
          <svg class="services__icon" viewBox="0 0 22 22"><circle cx="11" cy="11" r="9.5" fill="none" stroke="#fff" stroke-width="1.6"/><path d="M9 6.5 L13.5 11 L9 15.5" fill="none" stroke="#fff" stroke-width="1.8" stroke-linecap="round" stroke-linejoin="round"/></svg>
          Business Automation Services
        </li>
        <li class="services__item">
          <svg class="services__icon" viewBox="0 0 22 22"><circle cx="11" cy="11" r="9.5" fill="none" stroke="#fff" stroke-width="1.6"/><path d="M9 6.5 L13.5 11 L9 15.5" fill="none" stroke="#fff" stroke-width="1.8" stroke-linecap="round" stroke-linejoin="round"/></svg>
          AI (artificial intelligence integrations)
        </li>
      </ul>
    </section>

    <div class="illustration" role="img" aria-label="Isometric illustration of a rocket launching from a white platform, beside a rising bar chart with an upward arrow, a pie chart, a target and two gears"></div>
  </main>
</body>
</html>
```